Personalised Poetry business needs a business card designed

I am a writer that specialises in personalised poetry for people for significant life events.
I want a business card that stands out and portrays class and professionalism but is also welcoming & indicates warmth and honesty.
I'm happy with the logo that was designed for me, I would like to see it in raised print on the business card. I am open to suggestions on colours but think perhaps gold or silver writing for the logo would look good. I would like just the logo and my name and contact details on the front of the card. On the back of the card, I would like a list of the different events I provide poems for I will upload a photo of my current business card for reference. My current logo has a shading behind it that I don't like, I just want the words of the logo without any background colour

Target Market(s)

People wanting to provide a unique gift to someone special in their life

Industry/Entity Type

Writer

Contact Information for Business Card

Logo, my name and contact details on the front and a list of all the events I write poetry for on the back

Font styles to use
Script

Requirements
Must have
• I would like to see the logo, if possible, in a raised type of print on the card so that you can feel the actual words. I would like to have a glossy finish to the card and be able to print it on good quality board
Should not have
• The shading that is currently behind the logo on my current business card

```html
<!DOCTYPE html>
<html lang="en">
<head>
<meta charset="utf-8">
<title>Marlowe &amp; Finch – Business Card</title>
<link rel="stylesheet" href="https://fonts.googleapis.com/css2?family=Libre+Baskerville:wght@400;700&family=Open+Sans:wght@400;600&display=swap">
<style>
  :root {
    --stage: #2a2b2d;
    --card: #0d0d0e;
    --silver: #d9dadc;
    --silver-dim: #9a9b9e;
    --silver-light: #f4f4f5;
    --ink: #1b1b1c;
  }
  * { box-sizing: border-box; margin: 0; padding: 0; }
  html, body { width: 1200px; height: 952px; overflow: hidden; }
  body {
    background: radial-gradient(ellipse at 60% 50%, #3a3b3e 0%, var(--stage) 60%, #1c1d1f 100%);
    display: flex; align-items: center; justify-content: center; gap: 40px;
  }
  .card {
    position: relative; width: 540px; height: 310px;
    background: var(--card);
    box-shadow: 0 18px 40px rgba(0,0,0,.55);
  }
  .card-frame {
    position: absolute; inset: 12px;
    border: 1px solid var(--silver-dim);
  }
  /* Front */
  .brand-name {
    position: absolute; top: 74px; left: 150px; right: 40px; text-align: center;
    font-family: "Libre Baskerville", serif; font-weight: 400;
    font-size: 32px; color: var(--silver); letter-spacing: .5px;
  }
  .owner {
    position: absolute; left: 40px; top: 200px; width: 200px;
  }
  .owner-name {
    font-family: "Libre Baskerville", serif; font-weight: 700;
    font-size: 20px; color: var(--silver-light);
  }
  .owner-role {
    margin-top: 6px; font-family: "Open Sans", sans-serif; font-size: 13px; color: var(--silver);
  }
  .divider {
    position: absolute; left: 250px; top: 196px; width: 1px; height: 70px; background: var(--silver-dim);
  }
  .contact {
    position: absolute; left: 268px; top: 204px; list-style: none;
    font-family: "Open Sans", sans-serif; font-size: 15px; font-weight: 600; color: var(--silver-light);
  }
  .contact li { display: flex; align-items: center; gap: 10px; margin-bottom: 12px; white-space: nowrap; }
  .contact-icon {
    width: 20px; height: 20px; border-radius: 4px; background: var(--silver);
    display: flex; align-items: center; justify-content: center; flex: none;
  }
  /* Back */
  .quill-art {
    position: absolute; left: 40px; top: 30px; width: 130px; height: 150px;
    background: radial-gradient(ellipse at center, #3c3d40 0%, #1a1a1b 80%);
    border-radius: 6px;
  }
  .tagline {
    position: absolute; right: 12px; top: 66px; width: 260px; padding: 10px 18px;
    border-radius: 26px 0 0 26px;
    background: linear-gradient(90deg, #bfc0c3, #ffffff 60%, #d7d8da);
    font-family: "Libre Baskerville", serif; font-weight: 700; font-size: 15px;
    line-height: 1.3; color: var(--ink); text-align: center;
  }
  .events {
    position: absolute; right: 40px; top: 150px; list-style: none; text-align: right;
    font-family: "Open Sans", sans-serif; font-size: 15px; color: var(--silver-light);
  }
  .events li { display: flex; justify-content: flex-end; align-items: center; gap: 10px; margin-bottom: 7px; white-space: nowrap; }
  .tick { flex: none; }
</style>
</head>
<body>
  <section class="card card-front">
    <div class="card-frame"></div>
    <div class="brand-name">Marlowe &amp; Finch</div>
    <div class="owner">
      <div class="owner-name">Marcus Ellery</div>
      <div class="owner-role">Owner/ Writer</div>
    </div>
    <div class="divider"></div>
    <ul class="contact">
      <li>
        <span class="contact-icon">
          <svg width="12" height="12" viewBox="0 0 24 24" aria-hidden="true"><path d="M6.6 10.8a15 15 0 006.6 6.6l2.2-2.2c.3-.3.7-.4 1-.2 1.1.4 2.3.6 3.6.6.6 0 1 .4 1 1V20c0 .6-.4 1-1 1A17 17 0 013 4c0-.6.4-1 1-1h3.5c.6 0 1 .4 1 1 0 1.3.2 2.5.6 3.6.1.3 0 .7-.2 1z" fill="#0d0d0e"/></svg>
        </span>
        0400 555 123
      </li>
      <li>
        <span class="contact-icon">
          <svg width="12" height="12" viewBox="0 0 24 24" aria-hidden="true"><path d="M2 5h20v14H2z" fill="none" stroke="#0d0d0e" stroke-width="2.4"/><path d="M2 5l10 8 10-8" fill="none" stroke="#0d0d0e" stroke-width="2.4"/></svg>
        </span>
        marcus@marloweandfinch.com
      </li>
    </ul>
  </section>

  <section class="card card-back">
    <div class="card-frame"></div>
    <div class="quill-art" role="img" aria-label="Line drawing of a hand holding a fountain pen over a curling ribbon"></div>
    <div class="tagline">Momentous Life Events<br>Personalised in Poetry</div>
    <ul class="events">
      <li>Weddings &amp; Anniversaries <svg class="tick" width="14" height="14" viewBox="0 0 14 14" aria-hidden="true"><circle cx="7" cy="7" r="7" fill="#d9dadc"/><path d="M4 7.2l2 2 4-4" fill="none" stroke="#0d0d0e" stroke-width="1.6"/></svg></li>
      <li>Birthdays &amp; Christmas <svg class="tick" width="14" height="14" viewBox="0 0 14 14" aria-hidden="true"><circle cx="7" cy="7" r="7" fill="#d9dadc"/><path d="M4 7.2l2 2 4-4" fill="none" stroke="#0d0d0e" stroke-width="1.6"/></svg></li>
      <li>Valentines Day <svg class="tick" width="14" height="14" viewBox="0 0 14 14" aria-hidden="true"><circle cx="7" cy="7" r="7" fill="#d9dadc"/><path d="M4 7.2l2 2 4-4" fill="none" stroke="#0d0d0e" stroke-width="1.6"/></svg></li>
      <li>Retirements, Business &amp; Corporate Events <svg class="tick" width="14" height="14" viewBox="0 0 14 14" aria-hidden="true"><circle cx="7" cy="7" r="7" fill="#d9dadc"/><path d="M4 7.2l2 2 4-4" fill="none" stroke="#0d0d0e" stroke-width="1.6"/></svg></li>
      <li>Funerals &amp; Eulogies <svg class="tick" width="14" height="14" viewBox="0 0 14 14" aria-hidden="true"><circle cx="7" cy="7" r="7" fill="#d9dadc"/><path d="M4 7.2l2 2 4-4" fill="none" stroke="#0d0d0e" stroke-width="1.6"/></svg></li>
    </ul>
  </section>
</body>
</html>
```